Hair salon and Nail salon in Hawaii need a newspaper Ad design.

We need a newspaper Ad design for new open hair & nail salon in Waikiki Hawaii.Our Recommendation service for hair is "Head Spa" $30+tax and for nail is "Manicure Treatment Course" (Filing+Cuticle Care+Massage+Coloring) $20+tax.
We would like to see Hawaiian taste color and also having sense of luxury design. The ad size is W 5.0” x H 6.375”.
I would customers to know the shop place(Lanakila Crest Hotel 1F) , phone(808-555-0173), instagram(salonbrightwave) , our web site https://salonbrightwave.example and recommend services. For Web or Instagram , QR code is acceptable.

Target Market(s)

women & men

Industry/Entity Type

Beauty Salon

Font styles to use
Serif

Colors

Designer to choose colors to be used in the design.

Requirements
Must have
• Tagline for local customers. Shop Name is "SALON BRIGHTWAVE".the shop place(Lanakila Crest Hotel 1F) , phone(808-555-0173), instagram(salonbrightwave) and recommend services.
Nice to have
• Our services are competitive, but we don't want to be seen as just cheap and low quality.

```html
<!DOCTYPE html>
<html lang="en">
<head>
<meta charset="utf-8">
<title>Salon Brightwave – Newspaper Ad</title>
<link rel="stylesheet" href="https://fonts.googleapis.com/css2?family=Playfair+Display:wght@400;700&family=Roboto+Condensed:wght@300;400&display=swap">
<style>
  :root {
    --sand-light: #f1dcc0;
    --sand-mid: #e4c29a;
    --sand-deep: #d5ab7f;
    --maroon: #5a0f0f;
    --ink: #1c1614;
    --rose-gold: #d39a86;
    --rose-gold-dark: #b97a68;
    --white: #ffffff;
    --skin: #ecd3c2;
    --mat: #efe2cf;
  }
  * { margin: 0; padding: 0; box-sizing: border-box; }
  html, body { width: 1200px; height: 942px; overflow: hidden; background: var(--white); }
  .ad {
    position: relative; width: 1200px; height: 942px; overflow: hidden;
    font-family: "Playfair Display", Georgia, serif; color: var(--ink);
    background: var(--white);
  }
  .sand {
    position: absolute; left: 0; top: 0; width: 1200px; height: 790px;
    background: radial-gradient(ellipse at 75% 35%, var(--sand-light) 0%, var(--sand-mid) 55%, var(--sand-deep) 100%);
  }
  .sand-edge {
    position: absolute; left: 0; top: 782px; width: 1200px; height: 10px;
    background: linear-gradient(90deg, var(--rose-gold-dark), var(--rose-gold), #f0c6b4, var(--rose-gold));
  }
  .hero-photo {
    position: absolute; left: 0; top: 0; width: 560px; height: 752px;
    border-right: 9px solid var(--rose-gold);
    border-bottom: 9px solid var(--rose-gold);
    border-bottom-right-radius: 70px;
    background: linear-gradient(160deg, var(--mat) 0%, var(--skin) 45%, #e2b8a4 75%, var(--mat) 100%);
  }
  .frame {
    position: absolute; left: 570px; top: 36px; width: 594px; height: 693px;
    border: 1.5px solid var(--maroon); border-left: none;
  }
  .frame::before {
    content: ""; position: absolute; left: 0; top: 0; width: 1.5px; height: 0;
  }
  .accent-bar {
    position: absolute; left: 624px; top: 76px; width: 5px; height: 124px; background: var(--maroon);
  }
  .headline {
    position: absolute; left: 646px; top: 66px;
    font-weight: 700; font-size: 44px; line-height: 58px; color: var(--ink);
  }
  .headline-rule {
    position: absolute; left: 646px; top: 194px; width: 418px; height: 1.5px; background: var(--maroon);
  }
  .subhead {
    position: absolute; left: 646px; top: 208px;
    font-weight: 400; font-size: 35px; line-height: 48px; color: var(--ink);
    font-family: "Roboto Condensed", "Playfair Display", sans-serif; font-weight: 300;
  }
  .services {
    position: absolute; left: 646px; top: 345px; width: 476px; height: 178px;
    border-top: 1.5px solid var(--maroon); border-bottom: 1.5px solid var(--maroon);
    display: grid; grid-template-columns: 226px 250px; grid-template-rows: 78px 98px;
    font-family: "Roboto Condensed", sans-serif;
  }
  .services .cell { display: flex; flex-direction: column; align-items: center; justify-content: center; text-align: center; }
  .services .cell.right { border-left: 1.5px solid var(--maroon); }
  .services .cell.head { border-bottom: 1.5px solid var(--maroon); }
  .service-name { font-size: 22px; font-weight: 300; letter-spacing: 0.2px; }
  .service-note { font-family: "Playfair Display", serif; font-weight: 700; font-size: 14px; margin-top: 2px; }
  .service-detail { font-family: "Playfair Display", serif; font-size: 15.5px; line-height: 23px; }
  .price { font-family: "Playfair Display", serif; font-weight: 700; font-size: 21px; }
  .price small { font-weight: 400; font-size: 18px; }
  .hours {
    position: absolute; left: 647px; top: 547px; width: 316px; height: 35px;
    background: var(--maroon); color: var(--white);
    font-size: 15.5px; display: flex; align-items: center; justify-content: center;
  }
  .brand-card {
    position: absolute; left: 890px; top: 631px; width: 232px; height: 199px;
    background: var(--white); border: 7px solid var(--rose-gold);
    display: flex; flex-direction: column; align-items: center; justify-content: center; gap: 14px;
  }
  .brand-mark { width: 26px; height: 26px; background: var(--ink); }
  .brand-name { font-family: "Roboto Condensed", sans-serif; font-weight: 400; font-size: 19px; letter-spacing: 0.5px; color: var(--ink); }
  .side-bar {
    position: absolute; left: 1142px; top: 681px; width: 5px; height: 97px; background: var(--maroon);
  }
  .contact {
    position: absolute; right: 78px; top: 854px; text-align: right;
    font-family: "Roboto Condensed", sans-serif; font-size: 19.5px; line-height: 31px; color: var(--ink);
  }
  .contact b { font-family: "Playfair Display", serif; font-weight: 700; font-size: 18px; }
  .contact .sep { margin: 0 8px; }
</style>
</head>
<body>
<div class="ad">
  <div class="sand"></div>
  <div class="sand-edge"></div>
  <div class="hero-photo" role="img" aria-label="Photo of manicured hands resting on bare feet with French-tip nails and a pink lily on a bamboo mat"></div>

  <div class="frame"></div>
  <div class="accent-bar"></div>
  <h1 class="headline">We Groom You<br>To Look Beautiful!</h1>
  <div class="headline-rule"></div>
  <p class="subhead">A Hair &amp; Nail Salon In<br>Waikiki Hawaii</p>

  <div class="services">
    <div class="cell head">
      <span class="service-name">SERVICE FOR HAIR</span>
      <span class="service-note">(Head Spa)</span>
    </div>
    <div class="cell head right">
      <span class="service-name">SERVICE FOR NAILS</span>
      <span class="service-note">(Manicure Treatment Course)</span>
    </div>
    <div class="cell">
      <span class="price">$30 <small>+ tax</small></span>
    </div>
    <div class="cell right">
      <span class="service-detail">Filing + Cuticle Care +<br>Massage + Coloring</span>
      <span class="price">$20 <small>+ tax</small></span>
    </div>
  </div>

  <div class="hours">Visiting Hour: By Appointment Only</div>

  <div class="brand-card">
    <span class="brand-mark"></span>
    <span class="brand-name">SALON BRIGHTWAVE</span>
  </div>
  <div class="side-bar"></div>

  <div class="contact">
    <div>218 Kaiolu Lane, Honolulu, HI 96815, Lanakila Crest Hotel, 1st floor (Lower Lobby floor)</div>
    <div><b>Ph.:</b> 808 555 0173<span class="sep">|</span><b>W:</b> info@salonbrightwave.example<span class="sep">|</span><b>IG:</b> salonbrightwave<span class="sep">|</span><b>QR</b> code is acceptable</div>
  </div>
</div>
</body>
</html>
```